Provide bookkeeping and accounting services to small and growing businesses

We need website and logo design using the name Daltonby as the logo.
The target audience are small companies and startups who need:
1) Simple bookkeeping services
2) Accounting advice that only someone with many years of senior financial experience as a CPA can provide.

The services are provided by two individuals. each of whom specialize in one of the areas.

We want the website to be clean without a lot of visual distraction but don't know how to make a boring subject interesting. We believe our potential clients, small business owners, need to find what they want quickly and easily without a lot of verbiage or distractions.

We've attached a draft of the homepage and have completed the text on most of the other pages.

Target Market(s)

small and early stage growth companies in San Diego North County

Industry/Entity Type

Accounting

Number of Pages Required

1 page

Font styles to use
Sans Serif

Colors
86cfc6
33b8a4
85cae6

Requirements
Must have
• We need a design for the website homepage that includes the name Daltonby as the logo. Must include a design for the name.
• Must have color in teal or greenish blue.
Nice to have
• White background, clean, clear, uncluttered.
• We would like to use the design in a Theme on a WordPress website. Themes Maple Harbor and Copper Lantern are appealing to us.
Should not have
• Moving pictures

```html
<!DOCTYPE html>
<html lang="en">
<head>
<meta charset="utf-8">
<title>Daltonby Accounting &amp; Bookkeeping</title>
<link href="https://fonts.googleapis.com/css2?family=Roboto:wght@300;400;500;700&display=swap" rel="stylesheet">
<style>
:root{
  --teal:#33b8a4;
  --teal-soft:#86cfc6;
  --sky:#85cae6;
  --ink:#3a3a3a;
  --muted:#555;
  --rule:#d6d6d6;
  --panel:#e8e8e8;
}
*{margin:0;padding:0;box-sizing:border-box}
html,body{width:938px;height:1200px;overflow:hidden;background:#fff}
body{position:relative;font-family:'Roboto',Arial,sans-serif;color:var(--ink)}
.abs{position:absolute}
.top-rule{left:0;top:0;width:938px;height:4px;background:var(--teal-soft)}
.brand{left:58px;top:22px}
.brand-name{font-size:26px;font-weight:400;color:var(--teal);letter-spacing:.5px;line-height:1}
.brand-tag{font-size:10.5px;color:var(--muted);margin-top:3px;letter-spacing:.2px}
.contact-item{top:27px;font-size:11px;line-height:15px;color:#444;display:flex;gap:6px}
.contact-item b{font-weight:500;display:block}
.contact-item svg{margin-top:2px}
.main-nav{left:58px;top:77px;width:822px;height:30px;background:var(--sky);display:flex;align-items:center}
.main-nav a{color:#fff;text-decoration:none;font-size:13px;padding:0 14px 0 11px;border-right:1px solid rgba(255,255,255,.55);line-height:16px}
.main-nav a:first-child{padding-left:11px}
.social{display:flex;gap:3px}
.nav-social{right:0;top:3px;position:absolute;right:4px}
.social span{display:block;width:22px;height:22px;border:1.5px solid #fff;border-radius:50%}
.hero{left:0;top:114px;width:938px;height:360px;background:linear-gradient(100deg,#7a706c 0%,#9b8f8a 30%,#c9a8b4 50%,#d9d4d2 70%,#eef0f3 100%)}
.hero-title{left:58px;top:168px;color:#fff}
.hero-title h1{font-weight:400;font-size:46px;line-height:1}
.hero-title p{font-size:24px;font-weight:400;margin-top:2px}
.section-head{font-size:15px;font-weight:500;color:var(--ink);padding-bottom:9px;border-bottom:1px solid var(--rule)}
.section-head em{font-style:normal;color:var(--teal)}
.welcome{left:58px;top:492px;width:540px}
.welcome .section-head{width:340px}
.welcome p{margin-top:16px;font-size:11.6px;line-height:18.6px;color:#444}
.service{top:642px;width:260px}
.service-head{height:55px;color:#fff;font-size:14.5px;font-weight:500;line-height:15px;padding:12px 14px}
.service-photo{height:139px;margin-top:1px}
.service ul{list-style:none;margin-top:15px}
.service li{font-size:11.4px;line-height:21.6px;color:#444;padding-left:14px;position:relative}
.service li::before{content:"";position:absolute;left:2px;top:9px;width:4px;height:4px;border-radius:50%;background:var(--teal-soft)}
.news{left:642px;top:494px;width:238px}
.news .section-head{width:84px;font-size:14.5px}
.news-item{display:flex;gap:9px;padding:12px 0 10px;border-bottom:1px solid var(--rule);height:102px}
.news-item:last-child{border-bottom:none}
.news-list{margin-top:2px}
.date{width:49px;flex:none;height:57px;background:var(--sky);color:#fff;text-align:center}
.date .day{font-size:17.6px;font-weight:500;line-height:41px;height:43px}
.date .mon{font-size:9.5px;line-height:14px;border-top:1px solid #fff;background:#7ab8d2}
.news-body h3{font-size:10.5px;font-weight:700;line-height:15px;color:#333}
.news-body p{font-size:11px;line-height:15.5px;color:#555;margin-top:6px}
.news-body a{display:block;margin-top:4px;font-size:11px;color:var(--sky);text-decoration:none}
.newsletter{left:642px;top:836px;width:238px;height:115px;background:var(--panel);padding:14px 16px}
.newsletter h2{font-size:14.5px;font-weight:500;color:var(--ink)}
.newsletter h2 em{font-style:normal;color:var(--teal)}
.email-field{margin-top:9px;height:26px;background:#fff;border:1px solid #dcdcdc;font-size:11px;color:#999;padding:5px 10px}
.subscribe{margin-top:6px;height:25px;background:var(--sky);color:#fff;font-size:12.5px;font-weight:500;text-align:center;line-height:25px}
.site-footer{left:0;top:998px;width:938px;height:166px;background:var(--panel)}
.foot-col{top:1020px}
.foot-col h4{font-size:10.8px;font-weight:500;letter-spacing:.2px;color:#333}
.foot-col ul{list-style:none;margin-top:14px}
.foot-col li{font-size:11px;line-height:17.4px;color:#444}
.foot-col .gap{margin-top:11px}
.foot-social{margin-top:16px;gap:4px}
.foot-social span{width:26px;height:26px;border:1.5px solid #777}
.bottom-bar{left:0;top:1164px;width:938px;height:36px;background:var(--teal);color:#fff;font-size:11px;display:flex;justify-content:space-between;align-items:center;padding:0 58px 0 57px}
</style>
</head>
<body>
<div class="abs top-rule"></div>

<header>
  <div class="abs brand">
    <div class="brand-name">DALTONBY</div>
    <div class="brand-tag">ACCOUNTING &amp; BOOKKEEPING</div>
  </div>
  <div class="abs contact-item" style="left:662px">
    <svg width="11" height="11" viewBox="0 0 12 12"><path d="M2.5 1l2 2.3-1 1.2c.8 1.6 2 2.8 3.5 3.5l1.2-1L10.5 9 9.3 10.8C5 10.5 1.5 7 1.2 2.7z" fill="none" stroke="#33b8a4" stroke-width="1"/></svg>
    <div><b>Call Us:</b>1800 0000 000</div>
  </div>
  <div class="abs contact-item" style="left:766px">
    <svg width="13" height="10" viewBox="0 0 13 10"><rect x=".5" y=".5" width="12" height="9" fill="none" stroke="#85cae6"/><path d="M.5 .5l6 5 6-5" fill="none" stroke="#85cae6"/></svg>
    <div><b>Email Us:</b>info@daltonby.com</div>
  </div>
  <nav class="abs main-nav">
    <a href="#">HOME</a><a href="#">ABOUT US</a><a href="#">SERVICES</a><a href="#">EXPERIENCE</a><a href="#">RESOURCES</a><a href="#">CONTACT US</a>
    <div class="social nav-social" aria-label="Social links"><span></span><span></span><span></span><span></span></div>
  </nav>
</header>

<section class="abs hero" role="img" aria-label="Photo of three colleagues reviewing a colourful chart and a tablet at a desk"></section>
<div class="abs hero-title">
  <h1>Reliable</h1>
  <p>Accounting &amp; Bookkeeping</p>
</div>

<section class="abs welcome">
  <h2 class="section-head">Welcome to <em>Daltonby Accounting &amp; Bookkeeping</em></h2>
  <p>Daltonby offers a flexible range of accounting and bookkeeping services and support for small and growing organizations in San Diego North County.We provide bookkeeping services specializing in LedgerBooks® at your offices or remotely from ours. We also provide a broad range of accounting services or financial advice.</p>
</section>

<section class="abs service" style="left:58px">
  <div class="service-head" style="background:var(--teal)">Accounting<br>Services</div>
  <div class="service-photo" role="img" aria-label="Photo of business team meeting around a table" style="background:linear-gradient(120deg,#5a6470,#c7ccd2 50%,#e9ecef)"></div>
  <ul><li>Accounts payable</li><li>Billing and accounts receivable</li><li>Financial statement preparation</li><li>Payroll services</li><li>Daily deposit verification</li></ul>
</section>

<section class="abs service" style="left:339px">
  <div class="service-head" style="background:var(--teal-soft)">Bookkeeping<br>Services</div>
  <div class="service-photo" role="img" aria-label="Photo of hands working on a laptop with charts and paperwork" style="background:linear-gradient(120deg,#aab4bf,#e6e9ec 50%,#d8cfc4)"></div>
  <ul><li>Bank Reconciliation Reports</li><li>Budgeting Cash Flow Statement</li><li>Create Collections Process</li><li>Record Payments</li><li>Financial Dashboard</li></ul>
</section>

<aside class="abs news">
  <h2 class="section-head">Latest <em>News</em></h2>
  <div class="news-list">
    <article class="news-item"><div class="date"><div class="day">04</div><div class="mon">MAY</div></div>
      <div class="news-body"><h3>Lorem ipsum dolor sit amet, cons ectetur adipiscing elit,</h3><p>Sed ut perspiciatis unde omnis iste natus error sit voluptatem.</p><a href="#">Read More ›</a></div></article>
    <article class="news-item"><div class="date"><div class="day">03</div><div class="mon">MAY</div></div>
      <div class="news-body"><h3>Lorem ipsum dolor sit amet, cons ectetur adipiscing elit,</h3><p>Sed ut perspiciatis unde omnis iste natus error sit voluptatem.</p><a href="#">Read More ›</a></div></article>
    <article class="news-item"><div class="date"><div class="day">01</div><div class="mon">MAY</div></div>
      <div class="news-body"><h3>Lorem ipsum dolor sit amet, cons ectetur adipiscing elit,</h3><p>Sed ut perspiciatis unde omnis iste natus error sit voluptatem.</p><a href="#">Read More ›</a></div></article>
  </div>
</aside>

<section class="abs newsletter">
  <h2>Subscribe to &nbsp;<em>Our Newsletter</em></h2>
  <div class="email-field">Enter your email address</div>
  <div class="subscribe">SUBSCRIBE</div>
</section>

<footer>
  <div class="abs site-footer"></div>
  <div class="abs foot-col" style="left:57px"><h4>QUICK LINKS</h4>
    <ul><li>Home</li><li>About Us</li><li>Services</li><li>Experience</li><li>Resources</li><li>Contact Us</li></ul></div>
  <div class="abs foot-col" style="left:236px"><h4>SERVICES</h4>
    <ul><li>Bookkeeping</li><li>Controller Services</li><li>CFO Services</li><li>Accounting Systems &amp; Integration</li><li>Payroll</li></ul></div>
  <div class="abs foot-col" style="left:490px"><h4>CONTACT US</h4>
    <ul><li>Your Company LTD.</li><li>Street Name, 000000, City Name</li><li class="gap">Phone: 1-000-000-0000</li><li class="gap">Email: info@yourdomain.com</li></ul></div>
  <div class="abs foot-col" style="left:738px"><h4>FOLLOW US</h4>
    <div class="social foot-social" aria-label="Social links"><span></span><span></span><span></span><span></span></div></div>
  <div class="abs bottom-bar"><span>© 2016 &nbsp;Daltonby. All Rights Reserved</span><span>Privacy Policy | Terms of Service</span></div>
</footer>
</body>
</html>
```